Menu Board 1000mmx500mm re-design

I would like to re-design exiting menu board 1000mmx500mm. Current board letters are bit to small to read. I would like to have pictures (attached) of the food offered on it and at the same time to create balance between pictures and size of the text to be easily readable. Fonts and colours are up to designer choice but prefer warm and bright colours rather anything dark.

Target Market(s)

Food industry

Industry/Entity Type

Food

Font styles to use
Other font styles liked:
• I leave font choice to designer

Colors
FFC000
F8CF3A
FAE287
FDF2CF
FEFAEE
F0912C
F2A743
F7CA91
FBE8D2
FDF5EE
EE7325
F08F49
F5BC92
FAE3D3
FDF4ED

Requirements
Must have
• Pictures + Text
Nice to have
• Balance between images and text.
Should not have
• Can't think of any

```html
<!DOCTYPE html>
<html lang="en">
<head>
<meta charset="UTF-8">
<title>Menu Board</title>
<link rel="stylesheet" href="https://fonts.googleapis.com/css2?family=Anton&family=Great+Vibes&family=Poppins:wght@400;600;700;800&display=swap">
<style>
  :root {
    --backdrop: #e6e6e6;
    --board: #f2f2f3;
    --white: #ffffff;
    --ink: #1d1d1d;
    --orange: #e8561a;
    --orange-soft: #ee7325;
    --amber: #ffc000;
    --green: #1f6b35;
    --ring: #f08f49;
  }
  * { box-sizing: border-box; margin: 0; padding: 0; }
  html, body { width: 1200px; height: 1200px; overflow: hidden; }
  body { background: var(--backdrop); font-family: "Poppins", sans-serif; color: var(--ink); position: relative; }

  .board {
    position: absolute; left: 320px; top: 40px;
    width: 560px; height: 1120px;
    background: var(--board);
    overflow: hidden;
  }

  .disc { position: absolute; border-radius: 50%; }
  .disc-orange { left: 92px; top: 12px; width: 366px; height: 366px; background: var(--orange-soft); }
  .disc-amber { left: 169px; top: 11px; width: 360px; height: 360px; background: var(--amber); }

  .photo { position: absolute; border-radius: 50%; }
  .photo-potatoes {
    left: 129px; top: 4px; width: 360px; height: 360px;
    border: 4px solid var(--white);
    background: radial-gradient(circle at 45% 40%, #e9b45a 0%, #d58a2c 45%, #a85a1c 100%);
  }

  .thumb {
    position: absolute; border-radius: 50%;
    border: 1.5px solid var(--ring);
    padding: 6px; background: var(--white);
  }
  .thumb .photo { position: relative; width: 100%; height: 100%; }
  .thumb .dash {
    position: absolute; inset: 10px; border-radius: 50%;
    border: 1.5px dashed #3d6b4b; pointer-events: none;
  }
  .thumb-ciabatta { left: 9px; top: 38px; width: 156px; height: 156px; }
  .thumb-ciabatta .photo { background: radial-gradient(circle at 50% 50%, #c99a63 0%, #8a5a34 55%, #eceff2 72%); }
  .thumb-wrap { left: 36px; top: 216px; width: 184px; height: 184px; }
  .thumb-wrap .photo { background: radial-gradient(circle at 50% 45%, #e7dcc6 0%, #b58aa6 40%, #8a5a34 68%, #eceff2 80%); }
  .thumb-chicken { left: 290px; top: 228px; width: 262px; height: 262px; }
  .thumb-chicken .photo { background: radial-gradient(circle at 50% 50%, #d9a56a 0%, #8b5a33 45%, #6e4428 70%, #e9edf1 82%); }

  .title {
    position: absolute; left: 16px; top: 382px;
    font-family: "Great Vibes", cursive; font-size: 92px; line-height: 1;
    color: var(--orange);
  }

  .item { position: absolute; left: 32px; width: 425px; }
  .item h3 { font-weight: 800; font-size: 21px; line-height: 1.15; letter-spacing: 0.2px; }
  .item p { font-size: 17px; line-height: 1.55; font-weight: 400; }
  .line { display: flex; align-items: baseline; }
  .line span { white-space: nowrap; }
  .leader { flex: 1; border-bottom: 2px dotted var(--ink); margin-left: 4px; transform: translateY(-4px); }
  .item.solo h3 { display: flex; align-items: baseline; }
  .item.solo .leader { border-bottom-width: 3px; }

  .price {
    position: absolute; left: 463px; width: 69px; height: 29px;
    background: var(--orange);
    font-weight: 700; font-size: 22px; line-height: 29px;
    padding-left: 9px; color: var(--ink);
  }

  .sauces {
    position: absolute; left: 0; top: 1014px; width: 560px; height: 83px;
    background: var(--white);
  }
  .sauces h4 {
    position: absolute; left: 33px; top: 14px;
    font-family: "Anton", sans-serif; font-weight: 400; font-size: 40px; line-height: 1.2;
    letter-spacing: 0.5px;
  }
  .sauces .divider { position: absolute; left: 159px; top: 20px; width: 1.5px; height: 50px; background: var(--ink); }
  .sauce {
    position: absolute; font-weight: 700; font-size: 22px; line-height: 1;
    color: var(--orange); white-space: nowrap;
  }

  .stripe-amber { position: absolute; left: 0; top: 1093px; width: 560px; height: 4px; background: var(--amber); }
  .stripe-band {
    position: absolute; left: 0; top: 1097px; width: 560px; height: 23px;
    background: linear-gradient(90deg, var(--green) 0%, #8a6a22 45%, var(--orange-soft) 80%, var(--orange) 100%);
  }
</style>
</head>
<body>
  <div class="board">
    <div class="disc disc-orange"></div>
    <div class="disc disc-amber"></div>
    <div class="photo photo-potatoes" role="img" aria-label="Roasted potatoes with a rosemary sprig"></div>

    <div class="thumb thumb-ciabatta">
      <div class="photo" role="img" aria-label="Chicken ciabatta with rocket on a wooden board"></div>
      <div class="dash"></div>
    </div>
    <div class="thumb thumb-wrap">
      <div class="photo" role="img" aria-label="Grilled chicken wrap with slaw on a wooden board"></div>
      <div class="dash"></div>
    </div>
    <div class="thumb thumb-chicken">
      <div class="photo" role="img" aria-label="Roast chicken leg with veggie rice on a wooden plate"></div>
      <div class="dash"></div>
    </div>

    <div class="title">Menu</div>

    <div class="item" style="top:481px">
      <h3>CIABATTA</h3>
      <p>Roti Chicken, Rucola, Caramelized</p>
      <p class="line"><span>Tomato, Fresh Onion</span><i class="leader"></i></p>
    </div>
    <div class="price" style="top:528px">£6</div>

    <div class="item" style="top:564px">
      <h3>WRAP</h3>
      <p>Roti Chicken, Crunchy Slaw, Tomato, Fresh</p>
      <p class="line"><span>Onion &amp; Sauce of your Choice</span><i class="leader"></i></p>
    </div>
    <div class="price" style="top:606px">£7</div>

    <div class="item" style="top:648px">
      <h3>BEETROOT WRAP</h3>
      <p>Roti Chicken, Crunchy Slaw, Tomato, Fresh</p>
      <p class="line"><span>Onion &amp; Sauce of your Choice</span><i class="leader"></i></p>
    </div>
    <div class="price" style="top:696px">£8</div>

    <div class="item" style="top:738px">
      <h3>1/4 Chicken Box</h3>
      <p class="line"><span>Roti Chicken, Veggie Rice &amp; Salad</span><i class="leader"></i></p>
    </div>
    <div class="price" style="top:756px">£9</div>

    <div class="item" style="top:802px">
      <h3>1/2 Chicken Box</h3>
      <p class="line"><span>Roti Chicken, Veggie Rice &amp; Salad</span><i class="leader"></i></p>
    </div>
    <div class="price" style="top:822px">£14</div>

    <div class="item" style="top:866px">
      <h3>Roasted Potatoes</h3>
      <p class="line"><span>Thyme &amp; Garlic</span><i class="leader"></i></p>
    </div>
    <div class="price" style="top:884px">£2.5</div>

    <div class="item solo" style="top:926px">
      <h3><span>WATER</span><i class="leader"></i></h3>
    </div>
    <div class="price" style="top:924px">£1</div>

    <div class="item solo" style="top:964px">
      <h3><span>CAN &amp; JUICES</span><i class="leader"></i></h3>
    </div>
    <div class="price" style="top:962px">£1.8</div>

    <div class="sauces">
      <h4>SAUCES</h4>
      <div class="divider"></div>
      <span class="sauce" style="left:180px; top:18px">SIGNATURE</span>
      <span class="sauce" style="left:350px; top:18px">BBQ</span>
      <span class="sauce" style="left:435px; top:18px">PIRI PIRI</span>
      <span class="sauce" style="left:180px; top:46px">SWEET CHILLI</span>
      <span class="sauce" style="left:350px; top:46px">GARLIC MAYO</span>
    </div>

    <div class="stripe-amber"></div>
    <div class="stripe-band"></div>
  </div>
</body>
</html>
```